Advertising brochure for Trail Along Southside

We need a new single sided DL flier for the 2020 season!<br/>This flier is for our tour business. You can find all the details about the tour at our web site http://trailalong.southside.example<br/>The flier needs to grab the tourists attention, explain the tour and give price. I will upload a copy of last year's flier for your reference.<br/>We'd like the flier to match our web site to some extent.<br/>The most up to date information is on the web site and NOT last year's brochure. Use the web site for tour itinerary. We NO LONGER do the "Orchard Walk".<br/>Remember the size is "DL". Please no A4 format etc.<br/>You will be able to source images from:<br/>- Our web site<br/>- Our Chatterbook<br/>- Roamreview<br/>- Quarrel Listings<br/>If you have a particular idea in mind then feel free to contact us and we will try to accommodate your photo request.<br/>Good luck!

Target Market(s)

All ages

Industry/Entity Type

Tourism

Requirements
Must have
• Phone number
• Web Site
• Email address
• Price
Nice to have
• Description of tour and images

```html
<!DOCTYPE html>
<html lang="en">
<head>
<meta charset="utf-8">
<title>Trail Along Southside – DL Flier</title>
<link rel="stylesheet" href="https://fonts.googleapis.com/css2?family=Poppins:ital,wght@0,400;0,500;0,600;0,700;0,800;1,400;1,600;1,700;1,800&display=swap">
<style>
  :root {
    --orange: #ff6a06;
    --orange-light: #fbb062;
    --paper: #f7f7f7;
    --ink: #2b2b2b;
    --stage: #e8f1ee;
    --sand-a: #b9a58a;
    --sand-b: #d8c9b2;
    --caption-box: rgba(204, 122, 20, 0.82);
    --ghost: #e9e9e9;
  }
  * { margin: 0; padding: 0; box-sizing: border-box; }
  html, body { width: 1081px; height: 1200px; overflow: hidden; }
  body { background: var(--stage); font-family: "Poppins", sans-serif; position: relative; }

  .flier {
    position: absolute; left: 267px; top: 20px;
    width: 547px; height: 1160px;
    background: var(--paper); overflow: hidden;
    box-shadow: 0 10px 30px rgba(0,0,0,0.18);
  }
  .header-shape { position: absolute; left: 0; top: 0; }
  .side-ticks {
    position: absolute; left: 522px; top: 13px; width: 25px; height: 855px;
    background: repeating-linear-gradient(to bottom, var(--orange-light) 0 3.5px, transparent 3.5px 16px);
  }
  .ghost-region {
    position: absolute; left: 0; top: 345px; width: 547px; height: 560px;
    background: radial-gradient(ellipse at 70% 60%, var(--ghost) 0%, rgba(233,233,233,0) 60%);
  }
  .map-area {
    position: absolute; left: 242px; top: 45px; width: 201px; height: 181px;
    background: var(--orange-light); border-radius: 40% 45% 38% 30%;
  }
  .brand-small {
    position: absolute; left: 55px; top: 112px;
    color: #fff; font-weight: 500; font-size: 58px; line-height: 50px; letter-spacing: -2px;
  }
  .brand-rule {
    position: absolute; left: 56px; top: 236px; width: 382px; height: 2px; background: #fff;
  }
  .brand-large {
    position: absolute; left: 50px; top: 246px;
    color: #fff; font-weight: 800; font-style: italic; font-size: 58px; letter-spacing: -2px; line-height: 70px;
  }

  .stops { position: absolute; left: 0; top: 0; }
  .stop { position: absolute; left: 48px; width: 430px; }
  .stop-photo {
    position: absolute; left: 0; top: 0; width: 79px; height: 79px; border-radius: 50%;
    border: 1.5px solid var(--orange-light); padding: 4px;
  }
  .stop-photo span { display: block; width: 100%; height: 100%; border-radius: 50%; }
  .stop-copy { position: absolute; left: 91px; top: 0; width: 330px; }
  .stop-title { color: var(--orange); font-weight: 600; font-size: 16.5px; line-height: 20px; }
  .stop-text { color: var(--ink); font-style: italic; font-size: 14.2px; line-height: 17.5px; margin-top: 3px; }

  .tour-photo {
    position: absolute; left: 0; top: 868px; width: 482px; height: 222px;
    background: linear-gradient(160deg, var(--sand-b), var(--sand-a) 55%, #a89478);
  }
  .tour-photo.strip { top: 1147px; height: 13px; }
  .tour-caption {
    position: absolute; left: 35px; top: 967px; width: 323px; height: 113px;
    background: var(--caption-box); color: #fff;
    font-weight: 600; font-style: italic; font-size: 18.6px; line-height: 23.5px;
    padding: 8px 6px 0 8px; letter-spacing: -0.2px;
  }

  .price-badge { position: absolute; left: 360px; top: 895px; }
  .price-amount {
    position: absolute; left: 400px; top: 948px;
    color: #fff; font-weight: 800; font-style: italic; font-size: 64px; line-height: 64px; letter-spacing: -1px;
  }
  .price-unit {
    position: absolute; left: 393px; top: 1015px;
    color: #fff; font-size: 17px; letter-spacing: 3px; line-height: 20px;
  }
  .price-note {
    position: absolute; left: 395px; top: 1046px; width: 120px; text-align: center;
    color: #fff; font-weight: 700; font-size: 10px; line-height: 12px; transform: rotate(-3deg);
  }

  .contact-bar {
    position: absolute; left: 0; top: 1090px; width: 547px; height: 57px; background: var(--paper);
  }
  .phone {
    position: absolute; left: 35px; top: 12px;
    color: var(--orange); font-weight: 800; font-size: 28px; line-height: 34px; letter-spacing: -0.5px;
  }
  .contact-divider { position: absolute; left: 232px; top: 7px; width: 1px; height: 42px; background: var(--orange); }
  .contact-lines {
    position: absolute; left: 245px; top: 9px;
    color: var(--orange); font-style: italic; font-size: 12px; line-height: 18px;
  }
  .contact-lines b { font-weight: 800; margin-right: 6px; }
</style>
</head>
<body>
  <main class="flier">
    <div class="ghost-region" role="img" aria-label="Faint background map of the region"></div>

    <svg class="header-shape" width="547" height="400" viewBox="0 0 547 400" aria-hidden="true">
      <path d="M0 0 H547 V214 C450 320 330 390 216 383 C140 380 60 360 0 329 Z" fill="var(--orange)"/>
    </svg>
    <div class="side-ticks" aria-hidden="true"></div>

    <div class="map-area" role="img" aria-label="Map of the country in light orange"></div>
    <div class="brand-small">trail<br>along</div>
    <div class="brand-rule"></div>
    <div class="brand-large">SOUTHSIDE</div>

    <section class="stops">
      <article class="stop" style="top:406px">
        <div class="stop-photo"><span role="img" aria-label="Underground dugout living room" style="background:linear-gradient(135deg,#c9a58a,#7a4a3a)"></span></div>
        <div class="stop-copy" style="top:15px">
          <h2 class="stop-title">VISIT A MODERN UNDERGROUND DUGOUT</h2>
          <p class="stop-text">Step inside our underground home and see how a modern family lives in Ember Flats.</p>
        </div>
      </article>
      <article class="stop" style="top:492px">
        <div class="stop-photo"><span role="img" aria-label="Inside a working opal mine" style="background:linear-gradient(135deg,#6a6660,#2e2c29)"></span></div>
        <div class="stop-copy" style="top:9px">
          <h2 class="stop-title">VISIT AN OPAL MINE</h2>
          <p class="stop-text">Get a unique insight into opal mining as we show you how a real opal mine operates.</p>
        </div>
      </article>
      <article class="stop" style="top:578px">
        <div class="stop-photo"><span role="img" aria-label="Mining field landscape with spoil heaps" style="background:linear-gradient(180deg,#9a6a55,#6a3a2a)"></span></div>
        <div class="stop-copy" style="top:3px">
          <h2 class="stop-title">A SCENIC DRIVE THROUGH THE FIELD</h2>
          <p class="stop-text">View the magnificent scenery that over 100 years of terraforming has created from the comfort of your own car.</p>
        </div>
      </article>
      <article class="stop" style="top:664px">
        <div class="stop-photo"><span role="img" aria-label="Polished opal stone" style="background:radial-gradient(circle,#2a6a5a,#2a3a6a 60%,#eaeaea 62%)"></span></div>
        <div class="stop-copy" style="top:7px">
          <h2 class="stop-title">NOODLING FOR OPAL</h2>
          <p class="stop-text">Now it's time to find your very own opal by fossicking (Noodling) for your own. Our expert guide will show you how it's done.</p>
        </div>
      </article>
      <article class="stop" style="top:751px">
        <div class="stop-photo"><span role="img" aria-label="Opal being cut and polished" style="background:linear-gradient(135deg,#8a9a8a,#4a5a5a)"></span></div>
        <div class="stop-copy" style="top:14px">
          <h2 class="stop-title">CUTTING AND POLISHING</h2>
          <p class="stop-text">Learn how opals are cut and polished in the final stage of the opal journey.</p>
        </div>
      </article>
    </section>

    <div class="tour-photo" role="img" aria-label="Aerial view of tag-along cars driving through the opal fields"></div>
    <div class="tour-photo strip" aria-hidden="true"></div>
    <p class="tour-caption">Join our guide in a unique tag-along adventure around Ember Flats. Tour runs daily at 9am and for approx 3 hours.</p>

    <svg class="price-badge" width="200" height="200" viewBox="360 895 200 200" aria-hidden="true">
      <circle cx="460" cy="995" r="84" fill="var(--orange)"/>
      <path d="M416 950 A62 62 0 0 1 502 950" transform="translate(0,-10)" fill="none" stroke="#f4f4f4" stroke-width="4" stroke-linecap="round"/>
      <path d="M360 1060 A100 100 0 0 1 362 950" fill="none" stroke="#d8d8d8" stroke-width="4" stroke-linecap="round"/>
      <path d="M398 905 A100 100 0 0 1 550 915" fill="none" stroke="var(--orange)" stroke-width="4" stroke-linecap="round"/>
      <path d="M560 1030 A100 100 0 0 1 480 1095" fill="none" stroke="var(--orange)" stroke-width="4" stroke-linecap="round"/>
    </svg>
    <div class="price-amount">40$</div>
    <div class="price-unit">PER PERSON</div>
    <div class="price-note">kids half and children under 5 free</div>

    <footer class="contact-bar">
      <div class="phone">08 5550 1234</div>
      <div class="contact-divider"></div>
      <div class="contact-lines">
        <div><b>e.</b>hello@trailalong.southside.example</div>
        <div><b>w.</b>www.trailalong.southside.example</div>
      </div>
    </footer>
  </main>
</body>
</html>
```